Willow Creek Haven website design

To create 2 pages (a front page and sub page) for a health/spiritual website. I have a logo, and was thinking of incorporating Greek temple columns in the design or something similar, but open to other ideas.

The design should suit mobile devices with limited screen space also.

Industry/Entity Type

Health

Number of Pages Required

1 page

```html
<!DOCTYPE html>
<html lang="en">
<head>
<meta charset="utf-8">
<title>Willow Creek Haven</title>
<link rel="stylesheet" href="https://fonts.googleapis.com/css2?family=Cinzel:wght@400;700&family=Open+Sans:wght@400;600;700&display=swap">
<style>
:root{
  --gold:#f6a822;
  --white:#ffffff;
  --ink:#3a3a3a;
  --muted:#6d6d6d;
  --services:#17343a;
  --cyan:#26b5d6;
  --sage:#4d7e66;
  --deep-teal:#0e4a5e;
  --contact:#0b4456;
  --footer:#000000;
  --heading:"Cinzel",serif;
  --body:"Open Sans",sans-serif;
}
*{margin:0;padding:0;box-sizing:border-box}
html,body{width:1200px;height:3445px;overflow:hidden}
body{position:relative;background:var(--white);font-family:var(--body);color:var(--ink)}
section,header,footer{position:absolute;left:0;width:1200px}

/* hero */
.hero{top:0;height:597px;background:radial-gradient(ellipse at 50% 45%,#6b5634 0%,#3a2f22 35%,#15120e 70%,#0a0a0a 100%)}
.hero-photo{position:absolute;inset:0}
.brand{position:absolute;left:181px;top:22px;display:flex;align-items:center;gap:12px}
.brand-mark{width:40px;height:40px;border:2px solid rgba(255,255,255,.6)}
.brand-name{font-family:var(--heading);color:var(--white);font-size:17px;letter-spacing:1px}
.main-nav{position:absolute;right:176px;top:54px;display:flex;gap:22px}
.main-nav a{font-family:var(--heading);font-weight:700;font-size:13px;color:var(--white);text-decoration:none}
.main-nav a.active{color:var(--gold)}
.hero-title{position:absolute;top:222px;width:100%;text-align:center;font-family:var(--heading);color:var(--white);font-size:54px;line-height:86px;letter-spacing:1px}
.hero-title .accent{color:var(--gold)}
.hero-tagline{position:absolute;top:386px;width:100%;text-align:center;font-family:var(--heading);color:#ddd;font-size:22px;letter-spacing:2px}
.scroll-cue{position:absolute;left:578px;top:518px;width:44px;height:44px;border:3px solid var(--gold)}

/* section headings */
.section-title{font-family:var(--heading);color:var(--gold);font-size:22px;font-weight:700;letter-spacing:1px}
.title-rule{display:block;margin-top:6px}

/* about */
.about{top:597px;height:356px}
.about-text{position:absolute;left:0;top:0;width:683px;height:356px;background:var(--white)}
.about .section-title{position:absolute;left:184px;top:70px}
.about .title-rule{position:absolute;left:184px;top:100px}
.about-copy{position:absolute;left:216px;top:130px;width:410px;font-size:12px;line-height:26px;color:var(--muted);text-align:justify}
.read-more{font-family:var(--heading);color:var(--gold);font-size:14px;font-weight:700}
.about .read-more{position:absolute;right:92px;top:264px}
.about-photo{position:absolute;left:683px;top:0;width:517px;height:356px;background:linear-gradient(180deg,#c9cfd6 0%,#8f9aa6 45%,#2b2f35 85%,#111 100%)}

/* services */
.services{top:953px;height:385px;background:radial-gradient(ellipse at 60% 40%,#2a4a50 0%,var(--services) 55%,#0d2024 100%)}
.services .section-title{position:absolute;left:184px;top:70px}
.services .title-rule{position:absolute;left:184px;top:100px}
.service-card{position:absolute;top:138px;width:190px;height:184px}
.service-card .label{position:absolute;left:0;right:0;bottom:30px;text-align:center;font-family:var(--heading);font-size:15px;color:var(--white);line-height:20px}
.service-card.featured{border:3px solid var(--gold);background:#161616}
.service-card.featured .label{color:var(--gold)}
.card-1{left:190px}.card-2{left:398px;background:linear-gradient(160deg,#5b5b5b,#2a2a2a)}
.card-3{left:610px;background:linear-gradient(160deg,#7a6a3a,#2d2a1e)}.card-4{left:824px;background:linear-gradient(160deg,#4a2c2c,#1e1a1a)}

/* programs */
.programs{top:1338px;height:970px}
.programs .section-title{position:absolute;left:184px;top:72px}
.programs .title-rule{position:absolute;left:184px;top:102px}
.programs-intro{position:absolute;left:320px;top:132px;width:600px;text-align:center;font-size:14px;line-height:24px;color:var(--muted)}
.program-photo{position:absolute}
.program-box{position:absolute;color:var(--white);padding:26px 40px}
.program-box h3{font-family:var(--heading);font-size:19px;font-weight:700;margin-bottom:10px}
.program-box p{font-size:10.5px;line-height:18px;font-weight:600}
.box-health{left:445px;top:258px;width:571px;height:155px;background:var(--cyan);box-shadow:0 10px 16px rgba(0,0,0,.35)}
.box-health p{text-align:center}
.box-mind{left:184px;top:482px;width:568px;height:160px;background:var(--sage)}
.box-fitness{left:445px;top:714px;width:571px;height:158px;background:var(--deep-teal)}
.box-fitness p{text-align:center}
.box-icon{position:absolute;top:14px;width:16px;height:20px;border:2px solid rgba(0,0,0,.45);border-radius:50% 50% 40% 40%}
.box-health .box-icon,.box-fitness .box-icon{right:18px}
.box-mind .box-icon{left:20px;border-color:rgba(0,0,0,.35)}
.photo-health{left:184px;top:235px;width:261px;height:201px;background:linear-gradient(150deg,#b9c4cc,#5b6b7a 50%,#1f2838)}
.photo-mind{left:752px;top:464px;width:264px;height:196px;background:linear-gradient(180deg,#2b2f55 0%,#7b4a5c 55%,#d77a3c 80%,#2a1c18 100%)}
.photo-fitness{left:184px;top:694px;width:261px;height:195px;background:linear-gradient(135deg,#d9d3a0,#7d8a48 50%,#2f3a22)}

/* news */
.news{top:2308px;height:419px}
.news .section-title{position:absolute;left:184px;top:38px}
.news .title-rule{position:absolute;left:184px;top:68px}
.news-item{position:absolute;left:184px;width:832px;height:122px}
.news-item .thumb{position:absolute;left:0;top:0;width:190px;height:122px;background:linear-gradient(180deg,#e8e8e8,#9a9a9a 55%,#3c3c3c)}
.news-item h4{position:absolute;left:236px;top:0;font-family:var(--heading);color:var(--gold);font-size:15px;font-weight:700}
.news-item p{position:absolute;left:260px;top:22px;width:572px;font-size:10.5px;line-height:20px;color:var(--muted)}
.news-item .read-more{position:absolute;right:0;top:76px;font-size:11px}
.news-1{top:83px}.news-2{top:218px}

/* contact */
.contact{top:2727px;height:373px;background:var(--contact)}
.contact-icon{position:absolute;left:590px;top:50px;width:20px;height:14px;border:2px solid var(--gold);border-radius:3px}
.contact .section-title{position:absolute;top:72px;width:100%;text-align:center}
.field{position:absolute;left:253px;width:264px;height:38px;border:2px solid var(--white);color:var(--white);font-size:12px;font-weight:600;padding:9px 12px}
.field.active{border-color:var(--gold)}
.f-name{top:111px}.f-email{top:163px}.f-subject{top:215px}
.f-message{left:608px;top:111px;width:336px;height:147px}
.send{position:absolute;left:540px;top:290px;width:123px;height:40px;background:var(--gold);color:var(--white);font-weight:700;font-size:13px;text-align:center;line-height:40px}

/* footer */
.site-footer{top:3100px;height:345px;background:var(--footer);color:var(--white)}
.footer-col{position:absolute;top:60px}
.footer-col h5{font-family:var(--heading);color:var(--gold);font-size:15px;font-weight:700;margin-bottom:16px}
.footer-col li{list-style:none;font-size:12px;font-weight:600;line-height:25px}
.footer-col small{display:block;font-size:9px;color:#bbb;line-height:10px;margin-top:-6px;margin-bottom:4px}
.col-about{left:184px}.col-links{left:396px}.col-blogs{left:612px}.col-privacy{left:824px}
.footer-bar{position:absolute;left:0;top:310px;width:1200px;height:35px;border-top:1px solid #222;display:flex;align-items:center;justify-content:space-between;padding:0 170px 0 184px}
.footer-bar p{font-size:9.5px;color:#ccc}
.footer-bar b{color:var(--white)}
.social{display:flex;gap:8px}
.social span{width:13px;height:13px;background:#cfcfcf}
</style>
</head>
<body>

<header class="hero">
  <div class="hero-photo" role="img" aria-label="Night view of a floodlit classical temple with stone columns"></div>
  <div class="brand"><span class="brand-mark"></span><span class="brand-name">Willow Creek Haven</span></div>
  <nav class="main-nav">
    <a class="active" href="#">Home</a><a href="#">About</a><a href="#">Services</a><a href="#">Foundation Program</a><a href="#">Blog</a><a href="#">Contact</a>
  </nav>
  <h1 class="hero-title">Welcome To<br>Willow Creek <span class="accent">Haven</span></h1>
  <p class="hero-tagline">Mind * Body * Spirit</p>
  <svg class="scroll-cue" viewBox="0 0 44 44"><path d="M14 14l8 7 8-7M14 22l8 7 8-7" fill="none" stroke="#f6a822" stroke-width="3"/></svg>
</header>

<section class="about">
  <div class="about-text">
    <h2 class="section-title">About</h2>
    <svg class="title-rule" width="70" height="10"><line x1="0" y1="5" x2="70" y2="5" stroke="#f6a822" stroke-dasharray="3 3"/><rect x="31" y="1" width="7" height="7" fill="#f6a822" transform="rotate(45 34.5 4.5)"/></svg>
    <p class="about-copy">This is a sample version of Lorem Ipsum. Proin gravida nibh vel velit auctor aliquet. Aenean sollicitudin, lorem quis bibendum auctor, nisi elit consequat ipsum, nec sagittis sem nibh id elit. Duis sed odio sit amet nibh vulputate cursus a sit amet mauris. Morbi accumsan ipsum velit. Nam nec tellus a odio tincidunt auctor a ornare odio. Sed</p>
    <span class="read-more">Read More »</span>
  </div>
  <div class="about-photo" role="img" aria-label="Silhouette of a person in a yoga tree pose against a bright sky"></div>
</section>

<section class="services">
  <h2 class="section-title">Our Services</h2>
  <svg class="title-rule" width="70" height="10"><line x1="0" y1="5" x2="70" y2="5" stroke="#f6a822" stroke-dasharray="3 3"/><rect x="31" y="1" width="7" height="7" fill="#f6a822" transform="rotate(45 34.5 4.5)"/></svg>
  <div class="service-card card-1 featured" role="img" aria-label="Relaxation technique illustration"><span class="label">Relaxation<br>Technique</span></div>
  <div class="service-card card-2" role="img" aria-label="Pyramid yoga photo"><span class="label">Pyramid<br>Yoga</span></div>
  <div class="service-card card-3" role="img" aria-label="Person walking on a sunlit path"><span class="label">Weightless<br>Travel</span></div>
  <div class="service-card card-4" role="img" aria-label="Open book on a table"><span class="label">Book<br>Club</span></div>
</section>

<section class="programs">
  <h2 class="section-title">Foundation Program</h2>
  <svg class="title-rule" width="70" height="10"><line x1="0" y1="5" x2="70" y2="5" stroke="#f6a822" stroke-dasharray="3 3"/><rect x="31" y="1" width="7" height="7" fill="#f6a822" transform="rotate(45 34.5 4.5)"/></svg>
  <p class="programs-intro">This is a sample version of Lorem Ipsum. Proin gravida nibh vel velit auctor aliquet. Aenean sollicitudin, lorem quis bibendum auctor, nisi elit consequat ipsum, nec sagittis sem nibh id elit.</p>

  <div class="program-photo photo-health" role="img" aria-label="Hands holding fresh dark berries"></div>
  <div class="program-box box-health"><span class="box-icon"></span><h3>Health Program</h3><p>This is a sample version of Lorem Ipsum. Proin gravida nibh vel velit auctor aliquet. Aenean sollicitudin, lorem quis bibendum auctor, nisi elit consequat ipsum, nec sagittis sem nibh id elit. Duis sed odio sit amet nibh vulputate cursus a sit amet mauris. Morbi accumsan ipsum velit.</p></div>

  <div class="program-box box-mind"><span class="box-icon"></span><h3>Mind Program</h3><p>This is a sample version of Lorem Ipsum. Proin gravida nibh vel velit auctor aliquet. Aenean sollicitudin, lorem quis bibendum auctor, nisi elit consequat ipsum, nec sagittis sem nibh id elit. Duis sed odio sit amet nibh vulputate cursus a sit amet mauris. Morbi accumsan ipsum velit. Nam nec.</p></div>
  <div class="program-photo photo-mind" role="img" aria-label="Silhouette of a person stretching at sunset"></div>

  <div class="program-photo photo-fitness" role="img" aria-label="Woman running with a dog in a sunny park"></div>
  <div class="program-box box-fitness"><span class="box-icon"></span><h3>Fitness Program</h3><p>This is a sample version of Lorem Ipsum. Proin gravida nibh vel velit auctor aliquet. Aenean sollicitudin, lorem quis bibendum auctor, nisi elit consequat ipsum, nec sagittis sem nibh id elit. Duis sed odio sit amet nibh vulputate cursus a sit amet mauris. Morbi accumsan ipsum velit. Nam nec.</p></div>
</section>

<section class="news">
  <h2 class="section-title">Latest News</h2>
  <svg class="title-rule" width="70" height="10"><line x1="0" y1="5" x2="70" y2="5" stroke="#f6a822" stroke-dasharray="3 3"/><rect x="31" y="1" width="7" height="7" fill="#f6a822" transform="rotate(45 34.5 4.5)"/></svg>
  <article class="news-item news-1">
    <div class="thumb" role="img" aria-label="Hiker standing on a misty mountain ridge"></div>
    <h4>Lorem Ipsum, Proin</h4>
    <p>This is a sample version of Lorem Ipsum. Proin gravida nibh vel velit auctor aliquet. Aenean sollicitudin, lorem quis bibendum auctor, nisi elit consequat ipsum, nec sagittis sem nibh id elit. Duis sed odio sit amet nibh vulputate cursus a sit amet mauris. Morbi accumsan ipsum velit.</p>
    <span class="read-more">Read more »</span>
  </article>
  <article class="news-item news-2">
    <div class="thumb" role="img" aria-label="Hiker standing on a misty mountain ridge"></div>
    <h4>Lorem Ipsum, Proin</h4>
    <p>This is a sample version of Lorem Ipsum. Proin gravida nibh vel velit auctor aliquet. Aenean sollicitudin, lorem quis bibendum auctor, nisi elit consequat ipsum, nec sagittis sem nibh id elit. Duis sed odio sit amet nibh vulputate cursus a sit amet mauris. Morbi accumsan ipsum velit.</p>
    <span class="read-more">Read more »</span>
  </article>
</section>

<section class="contact">
  <span class="contact-icon"></span>
  <h2 class="section-title">Get In Touch</h2>
  <div class="field f-name active">Name</div>
  <div class="field f-email">Email</div>
  <div class="field f-subject">Subject</div>
  <div class="field f-message">Message</div>
  <div class="send">Send</div>
</section>

<footer class="site-footer">
  <div class="footer-col col-about"><h5>About</h5><ul><li>About Us</li><li>Careers</li><li>History</li><li>Staff</li></ul></div>
  <div class="footer-col col-links"><h5>Quick Links</h5><ul><li>Search</li><li>Articles</li><li>Foundation Program</li><li>Subscribe</li><li>Events</li></ul></div>
  <div class="footer-col col-blogs"><h5>Blogs</h5><ul><li>How to relax</li><small>by name</small><li>Relaxation Techniques</li><small>by name</small><li>Yoga in the Rain</li><small>by name</small><li>Reading in bed</li><small>by name</small></ul></div>
  <div class="footer-col col-privacy"><h5>Privacy</h5><ul><li>Privacy Statement</li><li>Terms &amp; Conditions</li><li>Comment Censorship</li><li>FAQ</li></ul></div>
  <div class="footer-bar">
    <p>Copyright © 2016 Willow Creek Haven. All rights reserved. Use of this site means you accept our <b>Site Agreement</b> and <b>Privacy Policy</b>.</p>
    <div class="social"><span></span><span></span><span></span><span></span></div>
  </div>
</footer>

</body>
</html>
```